Vista Chapel - Giving Hope
Sleek, Simple, Modern - Identity Package
Project: Vista Chapel - Giving Hope
Vista Chapel - Giving Hope - Religion and Spirituality
Creative Brief
Use specific fonts
open to new fonts and font changes
Simple
Ben Holloway
Chief Innovation Officer
4182 Cedar Vale Rd Atlanta, Ga 30319
404-561-3297 x 318
benh@cedarvalefold.org
www.CedarValeFold.org
Need a new fresh look for our letterhead, envelopes, labels, B. Cards etc. Also need the letterhead in Monarch size w/ matching envelopes. No deisgns that look like a law firm or accounting firm. Sleek and Modern is important.
Leave area on Back of card to make notes / write. The web address and/or some of the address info can go on the back. use our tag line someplace on the card: "Sharing Light Each Day"

```html
<!DOCTYPE html>
<html lang="en">
<head>
<meta charset="utf-8">
<title>Vista Chapel – Identity Package</title>
<link href="https://fonts.googleapis.com/css2?family=Open+Sans:wght@400;600;700&display=swap" rel="stylesheet">
<style>
:root{
  --ink:#121212;
  --blue:#1d8db5;
  --paper:#ffffff;
  --grey:#6b6b6b;
  --line:#cfd4d7;
  --copper-light:#e9b690;
  --copper:#b76f45;
  --copper-dark:#6e3a1f;
}
*{margin:0;padding:0;box-sizing:border-box}
html,body{width:1200px;height:737px;overflow:hidden}
body{
  font-family:"Open Sans",Arial,sans-serif;
  background:radial-gradient(ellipse at 45% 35%,var(--copper-light) 0%,var(--copper) 45%,var(--copper-dark) 100%);
  position:relative;
}
.piece{position:absolute;background:var(--paper);overflow:hidden;box-shadow:0 3px 10px rgba(0,0,0,.35)}
.piece svg.shape{position:absolute;inset:0;width:100%;height:100%}
.rays{position:absolute;inset:0;background:radial-gradient(ellipse at 15% 5%,#ffffff 0%,#f4f5f6 40%,#e9ebec 100%)}
.crosses{position:absolute;background:linear-gradient(180deg,rgba(150,150,150,0) 0%,rgba(150,150,150,.2) 100%)}
.crosses.dark{background:linear-gradient(180deg,rgba(255,255,255,0) 0%,rgba(255,255,255,.1) 100%)}
.brand{position:absolute;display:flex;align-items:center;white-space:nowrap}
.brand .dot{border-radius:50%;background:var(--ink);flex:none}
.brand .name{font-weight:700;color:var(--blue);letter-spacing:-.02em}
.brand.on-dark .dot{background:var(--blue)}
.brand.on-dark .name{color:var(--paper)}
.tagline{position:absolute;color:var(--blue);font-weight:600;white-space:nowrap}

.letterhead{left:29px;top:19px;width:535px;height:689px}
.letterhead .brand{left:16px;top:16px}
.letterhead .brand .dot{width:44px;height:44px;margin-right:8px}
.letterhead .brand .name{font-size:20px}
.letterhead .footer{position:absolute;left:0;right:0;top:643px;text-align:center;color:var(--paper);font-size:8.5px;line-height:14px}

.envelope{left:576px;top:24px;width:600px;height:372px}
.envelope .flap-brand{left:270px;top:6px;transform:rotate(180deg)}
.envelope .flap-brand .dot{width:16px;height:16px;margin-right:4px}
.envelope .flap-brand .name{font-size:9px}
.envelope .brand.main{left:18px;top:124px}
.envelope .brand.main .dot{width:52px;height:52px;margin-right:8px}
.envelope .brand.main .name{font-size:22px}
.envelope .return{position:absolute;left:180px;top:326px;font-size:8.5px;line-height:13px;color:var(--paper)}

.card{width:220px;height:133px}
.card-contact{left:638px;top:420px;background:var(--ink)}
.card-tag{left:905px;top:420px}
.card-notes{left:638px;top:563px}
.card-dark{left:905px;top:563px;background:var(--ink)}
.card-contact .details{position:absolute;left:10px;top:12px;color:var(--paper);font-size:5.5px;line-height:8px}
.card-contact .details .who{font-size:7px;font-weight:700}
.card-contact .details .gap{height:6px}
.card-contact .brand{left:82px;top:60px}
.card .brand .dot{width:28px;height:28px;margin-right:5px}
.card .brand .name{font-size:13px}
.card-tag .brand{left:50px;top:50px}
.card-tag .tagline{left:84px;top:82px;font-size:6px}
.card-notes .brand{left:112px;top:54px}
.card-notes .brand .dot{width:24px;height:24px;margin-right:4px}
.card-notes .brand .name{font-size:11px}
.card-notes .tagline{left:14px;top:112px;font-size:6px}
.notes-lines{position:absolute;left:12px;top:12px;width:100px}
.notes-lines span{display:block;height:13px;border-bottom:1px solid var(--line)}
.card-dark .brand{left:52px;top:50px}
.card-dark .tagline{left:86px;top:82px;font-size:6px}
</style>
</head>
<body>

<section class="piece letterhead" aria-label="Letterhead">
  <div class="rays"></div>
  <div class="crosses" style="left:110px;top:400px;width:270px;height:200px" role="img" aria-label="Faint hillside crosses"></div>
  <svg class="shape" viewBox="0 0 535 689" preserveAspectRatio="none">
    <path d="M0,606 Q267,542 535,606" fill="none" stroke="var(--blue)" stroke-width="3"/>
    <path d="M0,614 Q267,550 535,614 L535,689 L0,689Z" fill="var(--ink)"/>
  </svg>
  <div class="brand"><span class="dot"></span><span class="name">Vista Chapel</span></div>
  <p class="footer">4182 Cedar Vale Rd Atlanta, Ga 30319<br>Phone: 404-561-3297 x 318 | www.CedarValeFold.org</p>
</section>

<section class="piece envelope" aria-label="Envelope">
  <div class="crosses" style="left:340px;top:150px;width:200px;height:150px" role="img" aria-label="Faint hillside crosses"></div>
  <svg class="shape" viewBox="0 0 600 372" preserveAspectRatio="none">
    <path d="M0,0 H600 V34 Q300,66 0,34Z" fill="var(--ink)"/>
    <path d="M0,316 Q300,268 600,316" fill="none" stroke="var(--blue)" stroke-width="3"/>
    <path d="M0,323 Q300,275 600,323 V372 H0Z" fill="var(--ink)"/>
  </svg>
  <div class="brand on-dark flap-brand"><span class="dot"></span><span class="name">Vista Chapel</span></div>
  <div class="brand main"><span class="dot"></span><span class="name">Vista Chapel</span></div>
  <p class="return">4182 Cedar Vale Rd Atlanta, Ga 30319<br>Phone: 404-561-3297 x 318 | www.CedarValeFold.org</p>
</section>

<section class="piece card card-contact" aria-label="Business card front">
  <svg class="shape" viewBox="0 0 220 133" preserveAspectRatio="none">
    <path d="M126,0 Q78,66 126,133" fill="none" stroke="var(--blue)" stroke-width="3"/>
    <path d="M130,0 Q82,66 130,133 H220 V0Z" fill="var(--paper)"/>
  </svg>
  <div class="details">
    <div class="who">Ben Holloway</div>
    <div>Chief Innovation Officer</div>
    <div class="gap"></div>
    <div>4182 Cedar Vale Rd</div>
    <div>Atlanta, Ga 30319</div>
    <div class="gap"></div>
    <div>Phone: 404-561-3297 x 318</div>
    <div class="gap"></div>
    <div>benh@cedarvalefold.org</div>
    <div>Skype: benholl58</div>
  </div>
  <div class="brand"><span class="dot"></span><span class="name">Vista Chapel</span></div>
</section>

<section class="piece card card-tag" aria-label="Business card tagline side">
  <svg class="shape" viewBox="0 0 220 133" preserveAspectRatio="none">
    <path d="M0,0 Q30,66 0,133" fill="none" stroke="var(--blue)" stroke-width="3"/>
  </svg>
  <div class="brand"><span class="dot"></span><span class="name">Vista Chapel</span></div>
  <p class="tagline">Sharing Light Each Day</p>
</section>

<section class="piece card card-notes" aria-label="Business card notes side">
  <svg class="shape" viewBox="0 0 220 133" preserveAspectRatio="none">
    <path d="M136,0 Q108,66 136,133" fill="none" stroke="var(--blue)" stroke-width="2.5"/>
  </svg>
  <div class="notes-lines"><span></span><span></span><span></span><span></span><span></span></div>
  <div class="brand"><span class="dot"></span><span class="name">Vista Chapel</span></div>
  <p class="tagline">Sharing Light Each Day</p>
</section>

<section class="piece card card-dark" aria-label="Business card dark side">
  <div class="crosses dark" style="left:120px;top:72px;width:90px;height:61px" role="img" aria-label="Faint hillside crosses"></div>
  <div class="brand on-dark"><span class="dot"></span><span class="name">Vista Chapel</span></div>
  <p class="tagline">Sharing Light Each Day</p>
</section>

</body>
</html>
```